SEO Agentur www.findeprofi.de - Webseite soll neu designed werden (Start- und Unterseite)
Zielgruppe
Alle Infos sind auf der Seite www.findeprofi.de enthalten.
Aufgabenstellung
Die Seite soll neu gestalltet werden. Wir möchten gerne ein wenig professioneller werden. Der Name der Seite zwingt uns allerdings ein gewisses Thema auf.
Die Aufgabe:
Ein professionelleres Design der Startseite und einer Unterseite. Die Programmierung machen wir selbst. Thema Suche und Helden muss bleiben aufgrund der URL.
Mit dem Gewinner würden wir dann auch geren jedes Element der Seite durchgehen und neu gestallten (separater Auftrag).
Das Blitzwolf Logo ist aufgrund des neuen Films auch gewaltiger und seriöser geworden. Vielleicht kann man daran anknüpfen. Ist aber keine Bedingung nur eine kleine Idee.
Wir werden alle Vorschläge ca. 50 Leuten vorstellen und dann den Vorschlag mit den meisten Stimmen wählen.

```html
<!DOCTYPE html>
<html lang="de">
<head>
<meta charset="utf-8">
<title>Findeprofi – SEO Agentur</title>
<link href="https://fonts.googleapis.com/css2?family=Open+Sans:wght@400;600;700&display=swap" rel="stylesheet">
<style>
:root{
  --blue:#0f96e0;
  --blue-light:#25b4f0;
  --blue-dark:#0a6fb8;
  --blue-text:#1883cc;
  --red:#d0111b;
  --ink:#3a3a3a;
  --grey:#555;
  --topbar:#2d2f33;
  --footer:#393b40;
  --footer-bottom:#2a2b2f;
  --panel:#f3f4f8;
}
*{margin:0;padding:0;box-sizing:border-box}
html,body{width:787px;height:1200px;overflow:hidden}
body{position:relative;background:#fff;font-family:"Open Sans",Arial,sans-serif;color:var(--ink)}
.abs{position:absolute}
a{color:inherit;text-decoration:none}

.topbar{left:0;top:0;width:787px;height:20px;background:var(--topbar)}
.topbar .meta{left:150px;top:6px;font-size:5px;color:#ddd;display:flex}
.topbar .meta span{padding:0 8px;border-right:1px solid #666}
.topbar .meta span:first-child{padding-left:0}
.topbar .meta span:last-child{border:0}
.search{left:534px;top:3px;width:107px;height:13px;border-radius:4px;background:linear-gradient(#2ec0f7,#0c9be0)}

.navbar{left:0;top:20px;width:787px;height:34px;background:linear-gradient(#2bb7f3,#0b8ad6);border-top:1px solid #5fcdf9}
.nav{left:240px;top:34px;display:flex;font-size:6.6px;color:#fff;font-weight:600}
.nav span{padding:0 6px;border-right:1px solid rgba(0,0,0,.18)}
.nav span:last-child{border:0}
.brand{left:149px;top:21px;width:80px;height:60px;background:linear-gradient(#3a3c40,#1e1f22);display:flex;flex-direction:column;align-items:center;justify-content:center;gap:5px;box-shadow:0 2px 4px rgba(0,0,0,.4)}
.brand .name{font-size:10px;font-weight:700;color:var(--blue-light)}
.brand .dot{width:22px;height:22px;border-radius:50%;background:var(--blue-light)}

.slider{left:0;width:787px;background:radial-gradient(ellipse at 35% 40%,#f6f6f9 0%,#e4e9f0 45%,#b9cfe3 100%)}
.hero{top:54px;height:218px}
.hero-photo{left:425px;top:0;width:255px;height:218px;background:linear-gradient(#c7ccd3,#41464e 60%,#2b2e33)}
.slider h1{font-size:22px;font-weight:600;color:#3b3b3b;letter-spacing:-.3px}
.slider .sub{font-size:11px;color:var(--red)}
.slider p{font-size:11.3px;line-height:13px;color:#444}
.btn-l{width:87px;height:25px;border-radius:2px;background:linear-gradient(#27b3f2,#0a86d2);color:#fff;font-size:8.3px;font-weight:600;display:flex;align-items:center;justify-content:center;box-shadow:0 1px 2px rgba(0,0,0,.4)}
.arrow{width:22px;height:22px;border-radius:50%;background:radial-gradient(#fff,#dfe6ee);box-shadow:0 1px 3px rgba(0,0,0,.3)}
.dots{display:flex;gap:4px}
.dots i{width:7px;height:7px;border-radius:50%;background:#2a2d33}
.dots i:first-child{background:var(--blue)}
.shade{left:0;width:787px;height:10px;background:radial-gradient(ellipse at 50% 0,rgba(0,0,0,.35),transparent 70%)}

.tab{left:284px;width:221px;height:44px;background:linear-gradient(#29b5f3,#0a87d3);color:#fff;font-size:10.4px;font-weight:600;display:flex;align-items:center;justify-content:center;box-shadow:0 2px 3px rgba(0,0,0,.35);letter-spacing:.2px}

.service{top:328px;width:155px;text-align:center}
.service h2{font-size:12.5px;font-weight:600;color:var(--blue-text);margin-top:6px}
.service p{font-size:7.6px;line-height:10.8px;color:#555;text-align:justify;margin-top:3px;height:56px;letter-spacing:-.25px}
.service b{color:var(--red);font-weight:600}
.btn-s{display:inline-block;margin-top:11px;width:57px;height:16px;line-height:16px;font-size:5px;font-weight:600;color:#fff;background:linear-gradient(#29b3f1,#0a84cf);border-radius:1px}

.seo{top:511px;height:225px}
.seo-art{left:395px;top:0;width:392px;height:225px;background:linear-gradient(100deg,rgba(238,240,245,0) 0%,#eef1f5 12%,#e2dcd8 45%,#c9ab98 65%,#4a4d53 90%,#33363b 100%)}

.panel{left:149px;top:736px;width:491px;height:240px;background:linear-gradient(90deg,#eff1f6,#fff 50%,#f4f5f9)}
.side-btn{left:147px;width:119px;height:37px;background:linear-gradient(#29b5f3,#0a86d2);color:#fff;font-size:10.3px;font-weight:600;display:flex;align-items:center;gap:6px;padding-left:8px;box-shadow:0 2px 3px rgba(0,0,0,.35)}
.copy{left:283px;top:804px;width:344px;font-size:7.9px;line-height:10.8px;color:#555;text-align:justify;letter-spacing:-.15px}
.copy .lead{font-size:11.3px;line-height:14px;color:var(--red);text-align:left;margin:6px 0 7px;letter-spacing:-.3px}
.copy .lead span{color:var(--blue-text)}
.copy p+p{margin-top:5px}
.copy a{color:var(--blue-text);text-decoration:underline;font-weight:600}

.partners{left:149px;top:990px;width:491px;height:46px;display:flex}
.partners div{flex:1;border-left:1px solid #ddd;display:flex;align-items:center;justify-content:center;gap:4px;font-size:9px;color:#a8a8a8}
.partners div:last-child{border-right:1px solid #ddd}
.partners i{width:9px;height:9px;border-radius:50%;background:#c6c6c6}

.footer{left:0;top:1044px;width:787px;height:128px;background:var(--footer)}
.fcol{top:1058px;font-size:6.4px;line-height:9.3px;color:#eee}
.fcol h4{font-size:6.6px;color:var(--blue-light);font-weight:600}
.fcol h4.gap{margin-top:9px}
.fcol li{list-style:none;text-decoration:underline}
.fcol li::before{content:"› ";color:var(--blue-light)}
.contact{left:150px;top:1058px;font-size:7.4px;line-height:11.8px;color:#eee}
.contact h4{font-size:6.6px;color:var(--blue-light);font-weight:600;line-height:9px}
.social{left:150px;top:1140px;display:flex;gap:3px}
.social i{width:14px;height:14px;background:#b8b8b8;border-radius:2px}
.bottom{left:0;top:1172px;width:787px;height:28px;background:var(--footer-bottom);font-size:6.4px;color:#eee}
.bottom .copyr{left:150px;top:10px}
.bottom .copyr span{color:var(--blue-light)}
.bottom .acts{left:466px;top:11px;font-size:5.2px;display:flex;gap:20px}
.totop{left:621px;top:1177px;width:17px;height:17px;border-radius:50%;background:radial-gradient(#fff,#cfe3f3)}
</style>
</head>
<body>

<div class="abs topbar">
  <div class="abs meta"><span>IMPRESSUM</span><span>ÜBER UNS</span><span>KONTAKT</span></div>
  <div class="abs search">
    <svg class="abs" style="left:94px;top:2px" width="9" height="9" viewBox="0 0 10 10"><circle cx="4" cy="4" r="3" fill="none" stroke="#fff" stroke-width="1.2"/><path d="M6.2 6.2 9 9" stroke="#fff" stroke-width="1.4"/></svg>
  </div>
</div>

<div class="abs navbar"></div>
<nav class="abs nav"><span>ABLAUF</span><span>IHRE VORTEILE</span><span>UNSERE LEISTUNGEN</span><span>100 % GELD-ZURÜCK-GARANTIE</span><span>INFOS</span><span>BLOG</span><span>KONTAKT</span></nav>

<section class="abs slider hero">
  <div class="abs hero-photo" role="img" aria-label="Foto: Mann im Anzug öffnet sein Hemd und zeigt ein Heldenemblem"></div>
  <h1 class="abs" style="left:149px;top:50px">SEO Agentur Findeprofi</h1>
  <div class="abs sub" style="left:150px;top:85px">Erfolgsbasiert und mit 100% Geld-Zurück-Garantie</div>
  <p class="abs" style="left:150px;top:113px;width:270px">Wir halten was wir versprechen – <b style="font-weight:600">GARANTIERT!</b><br>Als einer der wenigen Anbieter geben wir Ihnen<br>eine 100% Geld-Zurück-Garantie!</p>
  <a class="abs btn-l" style="left:149px;top:165px">WEITER LESEN</a>
  <div class="abs arrow" style="left:43px;top:109px"><svg width="22" height="22"><path d="M13 6 8 11l5 5" fill="none" stroke="var(--blue)" stroke-width="2.5"/></svg></div>
  <div class="abs arrow" style="left:721px;top:109px"><svg width="22" height="22"><path d="M9 6l5 5-5 5" fill="none" stroke="var(--blue)" stroke-width="2.5"/></svg></div>
  <div class="abs dots" style="left:373px;top:203px"><i></i><i></i><i></i><i></i></div>
</section>

<a class="abs brand"><span class="name">findeprofi.de</span><span class="dot"></span></a>

<div class="abs shade" style="top:272px"></div>
<div class="abs tab" style="top:269px">UNSERE LEISTUNGEN IM ÜBERBLICK</div>

<div class="abs service" style="left:149px">
  <svg width="36" height="36" viewBox="0 0 36 36"><circle cx="18" cy="18" r="15" fill="none" stroke="var(--blue)" stroke-width="3.5"/><path d="M18 18V6M18 18l9 7" stroke="var(--blue)" stroke-width="3.5"/><circle cx="15" cy="20" r="4" fill="var(--blue)"/></svg>
  <h2>KEYWORD-ANALYSE</h2>
  <p>In Rahmen einer <b>detaillierten Analyse</b> Ihrer Website identifizieren wir mit Hilfe unserer SEO-Tools die für Sie relevanten Keywords. Sie erhalten von uns eine Übersicht mit den Angaben zu den Suchvolumina, ...</p>
  <a class="btn-s">WEITER LESEN</a>
</div>
<div class="abs service" style="left:318px">
  <svg width="36" height="36" viewBox="0 0 36 36"><circle cx="15" cy="15" r="11" fill="none" stroke="var(--blue)" stroke-width="3.5"/><path d="M23 23l9 9" stroke="var(--blue)" stroke-width="5" stroke-linecap="round"/></svg>
  <h2>DIE OPTIMIERUNG</h2>
  <p><b>Bei Searchly besser gesehen werden bedeutet für Sie mehr Umsatz.</b> Sie verstehen die Tätigkeiten Ihres Geschäftes und wir verstehen die Suchmaschinen. Möchten Sie mehr Kunden durch das Internet gewinnen?</p>
  <a class="btn-s">WEITER LESEN</a>
</div>
<div class="abs service" style="left:486px">
  <svg width="38" height="36" viewBox="0 0 38 36"><ellipse cx="19" cy="16" rx="16" ry="13" fill="none" stroke="var(--blue)" stroke-width="3.5"/><path d="M9 26 6 34l10-6" fill="var(--blue)"/><path d="M12 13h14M12 19h14" stroke="var(--blue)" stroke-width="3"/></svg>
  <h2>SEO CONSULTING</h2>
  <p>Damit Sie immer <b>einen Überblick über die Sichtbarkeit und den Verlauf</b> der Webseite in den Suchergebnissen haben, erhalten Sie in regelmäßigen Abständen Reportings über die aktuellen Rankingergebnisse ...</p>
  <a class="btn-s">WEITER LESEN</a>
</div>

<div class="abs shade" style="top:502px;transform:scaleY(-1)"></div>
<section class="abs slider seo">
  <div class="abs seo-art" role="img" aria-label="Foto: Hand mit Stift zeichnet ein SEO-Schaubild mit Begriffen wie Keywords, Content und Marketing"></div>
  <h1 class="abs" style="left:149px;top:36px">Was ist SEO?</h1>
  <div class="abs sub" style="left:150px;top:73px;color:#444">Kurz gesagt: <span style="color:var(--red)">Mehr Kunden und mehr Umsatz!</span></div>
  <p class="abs" style="left:150px;top:99px;width:310px">Unter dem Begriff SEO (Search Engine Optimization) versteht sich ein technischer Prozess, der Ihnen zu einer nachhaltigen Verbesserung bei den Suchergebnissen verhilft.</p>
  <a class="abs btn-l" style="left:149px;top:152px">WEITER LESEN</a>
  <div class="abs arrow" style="left:43px;top:105px"><svg width="22" height="22"><path d="M13 6 8 11l5 5" fill="none" stroke="var(--blue)" stroke-width="2.5"/></svg></div>
  <div class="abs arrow" style="left:721px;top:105px"><svg width="22" height="22"><path d="M9 6l5 5-5 5" fill="none" stroke="var(--blue)" stroke-width="2.5"/></svg></div>
  <div class="abs dots" style="left:373px;top:210px"><i></i><i></i><i></i><i></i></div>
</section>

<div class="abs panel"></div>
<div class="abs tab" style="top:734px">WIESO BRAUCHEN SIE SEO?</div>

<div class="abs side-btn" style="top:805px"><svg width="18" height="18" viewBox="0 0 18 18"><rect x="2" y="7" width="14" height="10" fill="none" stroke="#fff" stroke-width="1.5"/><rect x="1" y="5" width="16" height="3" fill="#fff"/><path d="M9 5v12" stroke="#fff" stroke-width="1.5"/></svg>IHRE VORTEILE</div>
<div class="abs side-btn" style="top:849px"><svg width="18" height="18" viewBox="0 0 18 18"><rect x="1" y="1" width="16" height="16" fill="none" stroke="#fff" stroke-width="1.5"/><path d="M4 14V11M7 14V9M10 14V8M13 14V5M3 9l4-3 3 2 5-4" stroke="#fff" stroke-width="1.5" fill="none"/></svg>MAßNAHMEN</div>
<div class="abs side-btn" style="top:893px"><svg width="18" height="18" viewBox="0 0 18 18"><rect x="1" y="1" width="16" height="16" fill="none" stroke="#fff" stroke-width="1.5"/><path d="M4 14l9-9" stroke="#fff" stroke-width="2"/></svg>UNSER SERVICE</div>

<div class="abs copy">
  <p>Durch neue Kunden im Internet wächst Ihr Unternehmen stabil, nachhaltig und kontrolliert. Durch unsere Arbeit erhalten Sie mehr Besucher, mehr Kunden und folglich mehr Umsatz!</p>
  <div class="lead">Mit Hilfe unserer Dienstleistung kommen Sie auf die ersten Plätze bei Searchly &amp; Co. <span>und bleiben dort auch langfristig.</span></div>
  <p>Bereits einer unseren ersten Kunden (ein mittelständischer Werkzeughandel aus Kassel) hat dank unserer Hilfe bereits nach 6 Monaten mit seinem Onlineshop eine monatliche Umsatzsteigerung von ca. 50%. Diese Umsatzsteigerung ist ausschließlich auf unsere Maßnahmen zurückzuführen.</p>
  <p>Lassen Sie das Internet nicht links liegen! Fordern Sie jetzt ein <a>kostenloses Angebot</a> für Ihre Optimierung an!</p>
</div>

<div class="abs shade" style="top:978px"></div>
<div class="abs partners">
  <div><i></i>Vogelwerk</div><div><i></i>Zukunftsplan</div><div>Hartwell</div><div><i></i>Brixcom</div><div>Olmera</div><div>Corvana</div>
</div>

<footer>
  <div class="abs footer"></div>
  <div class="abs contact">
    <h4>Kontakt</h4>
    Findeprofi GbR<br>Lindenweg 12<br>D - 49100 Musterstadt<br>
    <div style="margin-top:7px">Hotline: +49 (0)541/000 123 45<br>Wir warten auf Ihren Anruf</div>
  </div>
  <div class="abs social"><i></i><i></i><i></i><i></i><i></i><i></i></div>
  <div class="abs fcol" style="left:272px"><h4>Menü</h4><ul><li>Über uns</li><li>Ihre Vorteile</li><li>Wie es funktioniert?</li><li>100% Geld-zurück-Garantie</li><li>Kontakt</li><li>Suchmaschinenoptimierung</li><li>Homepageerstellung</li><li>Suchmaschinenwerbung</li><li>Social SEO</li><li>Blog</li></ul></div>
  <div class="abs fcol" style="left:374px"><h4>Suchmaschinenoptimierung</h4><ul><li>SEO Agentur</li><li>SEO Marketing</li><li>SEO Umsatz</li><li>Suchmaschinenoptimierung Agentur</li><li>SEO Agentur Erfolgsbasiert</li></ul><h4 class="gap">Webseiten</h4><ul><li>Webseiten Erstellung</li><li>Homepage erstellen lassen</li></ul></div>
  <div class="abs fcol" style="left:497px"><h4>Suchmaschinenwerbung</h4><ul><li>Adplus Agentur</li><li>Searchly Adplus</li><li>SEA Agentur</li><li>SEM Agentur</li></ul><h4 class="gap">Searchly Abstrafung</h4><ul><li>Searchly Abstrafung</li><li>Searchly Penalty</li></ul></div>
  <div class="abs fcol" style="left:593px"><h4>Erklärvideos</h4><ul><li>Erklärvideos</li><li>Erklärfilme</li><li>Produktvideos</li></ul></div>
  <div class="abs bottom">
    <div class="abs copyr">Copyright © 2014 <span>Findeprofi GbR</span></div>
    <div class="abs acts"><span>SEITE EMPFEHLEN</span><span>SEITE MERKEN</span></div>
  </div>
  <div class="abs totop"><svg width="17" height="17"><path d="M4 11l4.5-5 4.5 5" fill="none" stroke="var(--blue)" stroke-width="2.2"/></svg></div>
</footer>

</body>
</html>
```